Austrian company needs an advertising banner / fence design

title
Construction fence banner

description
The company Trofal GmbH is a company which specializes in scaffolding & amp; Specializes in rental.
We are looking for a banner design for the labeling of a construction fence.
The idea from our side:
To place a caricature (employee) on a scaffold at the bottom left and right of the banner. These Trofal employees hang up an advertising banner together with the company data.

Company data: Trofal GmbH
Scaffolding & amp; rental
www.trofal.at
0664 -58 29 384

Information regarding logo:
Color red: RAL 3020 Pantone 485 C
Font: Trajan Pro

```html
<!DOCTYPE html>
<html lang="en">
<head>
<meta charset="utf-8">
<title>Trofal GmbH – Construction Fence Banner</title>
<link href="https://fonts.googleapis.com/css2?family=Oswald:wght@500;600&family=Roboto+Mono:wght@700&display=swap" rel="stylesheet">
<style>
  :root {
    --page: #d4d4d4;
    --navy: #0b2a52;
    --navy-deep: #08234a;
    --navy-light: #123a6a;
    --signal-red: #d9141c;
    --rust: #a9492a;
    --white: #ffffff;
    --yellow: #ffe600;
    --pill: #2a1d1a;
    --workwear: #2d5bbf;
    --workwear-light: #4f7fd6;
  }
  * { box-sizing: border-box; margin: 0; padding: 0; }
  html, body { width: 963px; height: 1200px; overflow: hidden; }
  body { background: var(--page); position: relative; }

  .fence-banner {
    position: absolute; left: 20px; top: 362px;
    width: 923px; height: 475px;
    background: linear-gradient(180deg, var(--navy) 0%, var(--navy-deep) 75%, var(--navy-light) 88%, var(--navy-deep) 100%);
    box-shadow: 0 4px 14px rgba(0,0,0,.25);
    overflow: hidden;
  }

  .hanging-sign {
    position: absolute; left: 180px; top: 41px;
    width: 553px; height: 242px; overflow: hidden;
  }
  .sign-photo {
    position: absolute; inset: 0;
    background: linear-gradient(90deg, #e3b24a 0%, #c9812f 25%, #8d4b2c 60%, #6f6c84 85%, #5d7fb3 100%);
  }
  .sign-shape { position: absolute; inset: 0; }

  .sign-content {
    position: absolute; left: 0; top: 0; width: 523px; height: 100%;
    display: flex; flex-direction: column; align-items: center;
    font-family: 'Oswald', sans-serif;
  }
  .brand-name {
    margin-top: 21px;
    font-weight: 500; font-size: 26px; letter-spacing: 5px; line-height: 34px;
    color: var(--white);
  }
  .headline {
    margin-top: 6px; text-align: center;
    font-weight: 600; font-size: 52px; line-height: 55px;
    text-transform: uppercase; letter-spacing: -0.5px;
  }
  .headline .line-service { color: var(--white); display: block; }
  .headline .line-rental { color: var(--yellow); display: block; }

  .contact-row { margin-top: 15px; display: flex; gap: 16px; }
  .contact-pill {
    display: flex; align-items: center; gap: 7px;
    background: var(--pill); color: var(--white);
    border-radius: 11px; height: 22px; padding: 0 10px 0 5px;
    font-family: 'Oswald', sans-serif; font-weight: 600; font-size: 16px;
    white-space: nowrap;
  }
  .contact-pill.web { font-family: 'Roboto Mono', monospace; font-size: 14px; }
  .contact-pill svg { width: 15px; height: 15px; flex: none; }

  .worker {
    position: absolute;
    background: linear-gradient(180deg, #1f5fb5 0%, #e9e9e9 14%, var(--workwear-light) 30%, var(--workwear) 80%, #1b1b1b 100%);
    border-radius: 40px 40px 10px 10px;
    opacity: .95;
  }
  .worker-left { left: 96px; top: 64px; width: 118px; height: 395px; }
  .worker-right { left: 700px; top: 92px; width: 140px; height: 365px; }
</style>
</head>
<body>
  <section class="fence-banner">
    <div class="hanging-sign">
      <div class="sign-photo" role="img" aria-label="Photo of a building under construction wrapped in scaffolding with a crane at sunset"></div>
      <svg class="sign-shape" viewBox="0 0 553 242" preserveAspectRatio="none" aria-hidden="true">
        <ellipse cx="262" cy="121" rx="232" ry="260" fill="var(--rust)" fill-opacity=".85" stroke="var(--signal-red)" stroke-width="6"/>
      </svg>
      <div class="sign-content">
        <div class="brand-name">TROFAL</div>
        <h1 class="headline">
          <span class="line-service">Scaffolding &amp;</span>
          <span class="line-rental">Rental</span>
        </h1>
        <div class="contact-row">
          <div class="contact-pill phone">
            <svg viewBox="0 0 16 16"><circle cx="8" cy="8" r="8" fill="#fff"/><path d="M5.3 4.2l1.3 1.7-.7 1c.6 1.2 1.5 2.1 2.7 2.7l1-.7 1.7 1.3-.6 1.3c-3.2-.2-6.2-3.2-6.4-6.4z" fill="#2a1d1a"/></svg>
            0664 -58 29 384
          </div>
          <div class="contact-pill web">
            <svg viewBox="0 0 16 16"><circle cx="8" cy="8" r="8" fill="#fff"/><circle cx="8" cy="8" r="4.5" fill="none" stroke="#2a1d1a" stroke-width="1.2"/><path d="M3.5 8h9M8 3.5c-2 2.5-2 6.5 0 9M8 3.5c2 2.5 2 6.5 0 9" fill="none" stroke="#2a1d1a" stroke-width="1"/></svg>
            www.trofal.at
          </div>
        </div>
      </div>
    </div>
    <div class="worker worker-left" role="img" aria-label="Worker in blue overalls and hard hat carrying the left end of the sign"></div>
    <div class="worker worker-right" role="img" aria-label="Worker in blue overalls and hard hat carrying the right end of the sign on his shoulder"></div>
  </section>
</body>
</html>
```